Cover Page for Financial Statements

We need a cover page designed for our Financial Statements. It will need to include our business logo and the Chartered accountant logo.
We have included our current title page ( image titled full.png ) to show all the information that is needed to be included such as the title 'Financial Statements' and 'The year ended March 2023'. We would like to see designs that reflect our logo but also adds some interest with objects / deisngs that fill up more of the page.

Industry/Entity Type

Accounting

Font styles to use
Serif
Sans Serif

Colors

Designer to choose only greyscale colors for use in the design.

Requirements
Must have
• - A4 document size, our logo, Chartered Accountant Logo
Should not have
• Bright Colors

```html
<!DOCTYPE html>
<html lang="en">
<head>
<meta charset="utf-8">
<title>Clearline Accounting and Advisory Limited – Financial Statements</title>
<link rel="stylesheet" href="https://fonts.googleapis.com/css2?family=Bebas+Neue&family=PT+Sans:wght@400&display=swap">
<style>
  :root {
    --paper: #ffffff;
    --ink: #111111;
    --night: #000000;
    --wave-mid: #3a3a3a;
    --wave-dark: #0c0c0c;
    --badge: #9a9a9a;
    --canvas: #ffffff;
  }
  * { margin: 0; padding: 0; box-sizing: border-box; }
  html, body {
    width: 1200px; height: 1000px; overflow: hidden;
    background: var(--canvas);
  }
  .cover {
    position: absolute; left: 355px; top: 153px;
    width: 492px; height: 695px;
    background: var(--paper);
    overflow: hidden;
  }
  .cover__lower {
    position: absolute; left: 0; top: 272px;
    width: 100%; height: 423px;
    background: var(--night);
  }
  .brand {
    position: absolute; left: 19px; top: 24px;
    font-family: "Bebas Neue", sans-serif;
    color: var(--ink);
    line-height: 1;
  }
  .brand__name { font-size: 22px; letter-spacing: 2px; display: block; }
  .brand__tag { font-size: 9px; letter-spacing: 1.2px; display: block; margin-top: 3px; }
  .badge {
    position: absolute; left: 384px; top: 20px;
    width: 36px; height: 36px; border-radius: 50%;
    background: var(--badge);
  }
  .entity {
    position: absolute; left: -2px; top: 87px;
    width: 305px; height: 80px;
    border: 2px solid var(--ink);
    border-left: none;
    border-radius: 0 40px 40px 0;
    padding: 14px 0 0 21px;
    font-family: "Bebas Neue", sans-serif;
    font-size: 24px; letter-spacing: 1.6px; line-height: 26px;
    color: var(--ink);
  }
  .title {
    position: absolute; left: 31px; top: 196px;
    font-family: "Bebas Neue", sans-serif;
    font-size: 88px; line-height: 78px; letter-spacing: 6px;
  }
  .title__line { display: block; }
  .title__line--dark { color: var(--ink); }
  .title__line--light { color: var(--paper); }
  .period {
    position: absolute; left: 40px; top: 374px;
    font-family: "PT Sans", sans-serif;
    font-size: 14px; letter-spacing: 0.6px;
    color: var(--paper);
  }
  .waves {
    position: absolute; left: 0; top: 410px;
    width: 100%; height: 270px;
    background: radial-gradient(ellipse at 50% 45%, var(--wave-mid) 0%, #1e1e1e 45%, var(--wave-dark) 80%);
    opacity: 0.85;
  }
  .arrow {
    position: absolute; left: 405px; top: 607px;
    width: 58px; height: 58px;
  }
</style>
</head>
<body>
  <main class="cover">
    <div class="cover__lower"></div>

    <div class="brand">
      <span class="brand__name">Clearline</span>
      <span class="brand__tag">Accounting &amp; Advisory</span>
    </div>
    <div class="badge" aria-hidden="true"></div>

    <div class="entity">Clearline Accounting<br>and Advisory Limited</div>

    <h1 class="title">
      <span class="title__line title__line--dark">Financial</span>
      <span class="title__line title__line--light">Statements</span>
    </h1>

    <p class="period">FOR THE YEAR ENDED 31 MARCH 2023</p>

    <div class="waves" role="img" aria-label="Flowing grey line-wave decoration"></div>

    <svg class="arrow" viewBox="0 0 58 58" aria-hidden="true">
      <path d="M4 54 L52 6 M14 4 H54 V44" fill="none" stroke="#ffffff" stroke-width="6" stroke-linecap="square"/>
    </svg>
  </main>
</body>
</html>
```